Cover-Design für Collegeblockserie
Zielgruppe
Wir sind ein Anbieter von Papierprodukten wie Hefte, Collegeblöcke und gebundene Bücher für den Schul- und Officebereich. In jedem Jahr bringne wir eine Collegeblockserie heraus mit einem limitierten Coverdesign.
Weitere Infos zu uns und der Aufgabe können dem beigefügten Briefing entnommen werden.
Aufgabenstellung
Vorgaben können dem Breifing entnommen werden

```html
<!DOCTYPE html>
<html lang="de">
<head>
<meta charset="utf-8">
<title>Collegeblock Cover – Power in your hands</title>
<link rel="stylesheet" href="https://fonts.googleapis.com/css2?family=Oswald:wght@600&family=Allura&display=swap">
<style>
  :root {
    --page-bg: #f2f2f2;
    --cover-white: #ffffff;
    --tone-yellow: #fde0a0;
    --tone-pink: #ef8e92;
    --tone-teal: #9fd6d6;
    --ink-black: #111111;
    --brand-navy: #2b1b8c;
  }
  html, body {
    margin: 0;
    padding: 0;
    width: 1200px;
    height: 1200px;
    overflow: hidden;
    background: var(--page-bg);
  }
  .canvas {
    position: relative;
    width: 1200px;
    height: 1200px;
  }
  .cover {
    position: absolute;
    left: 246px;
    top: 50px;
    width: 708px;
    height: 1100px;
    background: var(--cover-white);
    box-shadow: 0 0 0 1px #e2e2e2;
    overflow: hidden;
  }
  .cover-artwork {
    position: absolute;
    inset: 0;
    background:
      radial-gradient(ellipse 340px 380px at 220px 300px, var(--tone-yellow) 0%, rgba(253,224,160,0.85) 45%, rgba(253,224,160,0) 100%),
      radial-gradient(ellipse 300px 480px at 560px 460px, var(--tone-pink) 0%, rgba(239,142,146,0.85) 50%, rgba(239,142,146,0) 100%),
      radial-gradient(ellipse 300px 360px at 520px 880px, var(--tone-teal) 0%, rgba(159,214,214,0.85) 45%, rgba(159,214,214,0) 100%),
      var(--cover-white);
  }
  .brand {
    position: absolute;
    left: 102px;
    top: 127px;
    display: flex;
    align-items: center;
    gap: 8px;
  }
  .brand-mark {
    width: 22px;
    height: 22px;
    background: var(--brand-navy);
  }
  .brand-name {
    font-family: "Oswald", sans-serif;
    font-weight: 600;
    font-size: 40px;
    line-height: 1;
    color: var(--brand-navy);
  }
  .tagline {
    position: absolute;
    left: 524px;
    top: 566px;
    margin: 0;
    transform: translate(-50%, -50%) rotate(90deg);
    white-space: nowrap;
    font-family: "Allura", cursive;
    font-weight: 400;
    font-size: 80px;
    line-height: 1;
    color: var(--ink-black);
  }
</style>
</head>
<body>
<div class="canvas">
  <div class="cover">
    <div class="cover-artwork" role="img" aria-label="Abstrakte Farbflächen in Pastellgelb, Rosa und Türkis mit einer geschwungenen schwarzen Linie"></div>
    <div class="brand">
      <span class="brand-mark"></span>
      <span class="brand-name">Feldmark</span>
    </div>
    <p class="tagline">Power in your hands</p>
  </div>
</div>
</body>
</html>
```